4' x 8' Construction Project Sign, think of a very large business card

We need project signs for our construction sites, the sign will be mounted along the road so cars driving by can quickly read. the sign should be able to be read as cars drive by doing highway speed.

Think like your making a large business card

I would like to include "NOW HIRING" Superintendents, Project Managers, Pipe Foremen, Pipe Layers, and Equipment Operators

Description of services we provide should include

Civil Construction Services
Land Clearing
Excavation
Underground Utilities
Environmental Maintenance

The 2 objectives is to market to future clients and to recruit new employees

The sign will be mounted on posts at the entrance of our construction projects
Updates

Low design quality

Target Market(s)

Construction and land developers

Industry/Entity Type

Construction Company

Other font styles liked:
• Hypatia Sans Pro lite

Colors

Designer to choose colors to be used in the design.

Requirements
Must have
• Clean and easy to read
• Civil Construction Services
• Land Clearing
• Excavation
• Underground Utilities
• Road Construction

```html
<!DOCTYPE html>
<html lang="en">
<head>
<meta charset="utf-8">
<title>Now Hiring – Harlan Sitework Co.</title>
<link rel="stylesheet" href="https://fonts.googleapis.com/css2?family=Open+Sans:wght@400;600;800&display=swap">
<style>
  :root {
    --brand-blue: #0a22b8;
    --panel-dark: #303030;
    --sign-white: #ffffff;
    --tag-fill: #f2f3f7;
  }
  html, body {
    margin: 0;
    padding: 0;
    width: 1200px;
    height: 600px;
    overflow: hidden;
    background: var(--panel-dark);
  }
  .sign {
    display: block;
    width: 1200px;
    height: 600px;
    font-family: "Open Sans", Arial, sans-serif;
  }
  .sign-frame { fill: var(--panel-dark); }
  .headline-band { fill: var(--sign-white); }
  .headline { fill: var(--brand-blue); font-size: 172px; }
  .headline-regular { font-weight: 400; }
  .headline-bold { font-weight: 800; }
  .services-panel { fill: var(--panel-dark); }
  .roles-panel { fill: var(--brand-blue); }
  .divider { stroke: var(--sign-white); stroke-width: 9; fill: none; }
  .list-item { fill: var(--sign-white); font-size: 38px; font-weight: 600; }
  .services .list-item { text-anchor: end; }
  .company-tag { fill: var(--tag-fill); }
  .company-name { fill: var(--panel-dark); font-size: 24px; font-weight: 600; text-anchor: middle; }
</style>
</head>
<body>
<svg class="sign" viewBox="0 0 1200 600" xmlns="http://www.w3.org/2000/svg">
  <rect class="sign-frame" x="0" y="0" width="1200" height="600"/>
  <rect class="headline-band" x="11" y="11" width="1178" height="167"/>
  <text class="headline" x="57" y="159" textLength="1085" lengthAdjust="spacingAndGlyphs"><tspan class="headline-regular">NOW </tspan><tspan class="headline-bold">HIRING</tspan></text>

  <rect class="services-panel" x="19" y="190" width="1162" height="389"/>
  <polygon class="roles-panel" points="19,190 507,190 611,384 502,579 19,579"/>
  <polyline class="divider" points="514,186 617,384 507,584"/>

  <g class="roles">
    <text class="list-item" x="59" y="258">Superintendents</text>
    <text class="list-item" x="59" y="327">Project Managers</text>
    <text class="list-item" x="59" y="396">Pipe Foremen</text>
    <text class="list-item" x="59" y="466">Pipe Layers</text>
    <text class="list-item" x="59" y="535">Equipment Operators</text>
  </g>

  <g class="services">
    <text class="list-item" x="1141" y="258">Civil Construction Services</text>
    <text class="list-item" x="1141" y="327">Underground Utilities</text>
    <text class="list-item" x="1141" y="396">Land Clearing</text>
    <text class="list-item" x="1141" y="466">Excavation</text>
    <text class="list-item" x="1141" y="535">Environmental Maintenance</text>
  </g>

  <g class="company">
    <rect class="company-tag" x="470" y="366" width="260" height="46" rx="23"/>
    <text class="company-name" x="600" y="397">Harlan Sitework Co.</text>
  </g>
</svg>
</body>
</html>
```